Web Design Project

This is a wordpress project for a newly formed biologics company based in the US with international clientele. We do manufacturing of biologically based raw materials using a state of the art facility....Our logo must be incorporated....logo colors Navy and Gray. It is fine to use some color in web design. The viewer will primarily be industry folk.

Velorast Biologics, LLC is a contract manufacturing organization which produces biologically-based raw materials derived primarily from human plasma. The company services include extraction and purification of plasma components, especially proteins and enzymes. The business focuses on biotherapeutics, diagnostic and veterinary markets worldwide.

5 pages a bad example of first page can be found in attached files.....
use stock photos of labs and clean rooms.
Updates

Project Deadline Extended
Reason: I need a bit more time tonprovide feedback.

Project Deadline Extended
Reason: needed time to evaluate existing options

Target Market(s)

target market Pharmaceutical companies and research universities

Industry/Entity Type

Veterinary

Requirements
Must have
• our logo...we will provide some graphics...

```html
<!DOCTYPE html>
<html lang="en">
<head>
<meta charset="utf-8">
<title>Velorast Biologics</title>
<link rel="stylesheet" href="https://fonts.googleapis.com/css2?family=Arimo:ital,wght@0,400;0,700;1,400;1,700&display=swap">
<style>
:root{
  --navy:#0f4c8a;
  --heading:#144a82;
  --text:#575757;
  --nav-top:#2a78c0;
  --nav-bottom:#004a8d;
  --panel:#e9e9e9;
  --panel-line:#c9c9c9;
  --footer:#2c5f9a;
  --white:#ffffff;
}
*{box-sizing:border-box;margin:0;padding:0}
html,body{width:1050px;height:1200px;overflow:hidden;background:var(--white)}
body{position:relative;font-family:"Arimo",Arial,sans-serif;color:var(--text)}
.abs{position:absolute}
.header-swoosh{left:0;top:0}
.brand{left:72px;top:20px;display:flex;align-items:center;gap:6px}
.brand-mark{width:66px;height:66px;border-radius:50%;background:var(--navy)}
.brand-name{font-size:25px;font-weight:700;color:var(--navy);letter-spacing:-0.5px}
.search{left:826px;top:57px;width:156px;height:33px;border:1px solid #c8c8c8;border-radius:8px;background:var(--white);box-shadow:inset 0 1px 2px rgba(0,0,0,.08)}
.search-label{position:absolute;left:13px;top:9px;font-size:12px;font-style:italic;color:#222}
.search-icon{position:absolute;right:7px;top:4px}
.main-nav{left:50px;top:107px;width:951px;height:37px;border-radius:7px;border:1px solid #7aa6d3;background:linear-gradient(var(--nav-top),var(--nav-bottom) 55%,#003f7a);box-shadow:0 1px 2px rgba(0,0,0,.3)}
.main-nav a{position:absolute;top:11px;font-size:13px;color:var(--white);text-decoration:none}
.hero{left:58px;top:164px;width:931px;height:282px;border-radius:8px;border-right:2px solid #1d4f8c;background:radial-gradient(ellipse at 30% 60%,#dfe3ec 0%,#b9c2d6 45%,#8f9cb8 100%)}
.hero-dots{position:absolute;left:862px;top:255px;display:flex;gap:5px}
.hero-dots span{width:12px;height:12px;border-radius:50%;background:#d9d9d9;border:1px solid #a8a8a8}
.hero-dots .is-active{background:#3e8fd6;border-color:#1d5b9c}
h2{font-weight:400;font-size:18px;color:var(--heading)}
p{font-size:12px;line-height:18px;color:var(--text)}
.photo{background:linear-gradient(135deg,#e9eef3,#b9c6d3)}
.section-rule{left:69px;top:766px;width:626px;height:1px;background:#555}
.member-name{font-size:14px;font-weight:700;font-style:italic;color:#666}
.side-box{left:726px;width:275px;border-radius:7px;border:1px solid #d6d6d6;background:var(--panel);overflow:hidden}
.side-head{height:46px;padding:15px 12px 0;background:linear-gradient(#ffffff,#e3e3e3);border-bottom:1px solid var(--panel-line)}
.btn-more{left:882px;top:964px;width:105px;height:27px;border-radius:7px;border:1px solid #7fb0dd;background:linear-gradient(var(--nav-top),var(--nav-bottom));color:var(--white);font-size:13px;text-align:center;line-height:27px;box-shadow:0 1px 2px rgba(0,0,0,.35)}
.site-footer{left:50px;top:1105px;width:951px;height:95px;background:var(--footer);color:var(--white);font-size:12px}
.footer-links{position:absolute;left:26px;top:18px}
.footer-links a{color:var(--white);text-decoration:none}
.copyright{position:absolute;left:26px;top:38px}
.connect{position:absolute;left:799px;top:18px}
.social{position:absolute;left:799px;top:40px;display:flex;gap:5px}
.social span{width:21px;height:21px;border-radius:50%;background:var(--white)}
</style>
</head>
<body>

<svg class="abs header-swoosh" width="1050" height="110" viewBox="0 0 1050 110" aria-hidden="true">
  <path d="M200 106 C420 60 640 20 1000 0 L1000 106 Z" fill="#f1f1f1"/>
  <path d="M820 40 C880 20 940 10 1000 10 L1000 0 C930 3 870 15 820 40 Z" fill="#e4e4e4"/>
</svg>

<div class="abs brand">
  <span class="brand-mark"></span>
  <span class="brand-name">Velorast Biologics</span>
</div>

<div class="abs search">
  <span class="search-label">Seach</span>
  <svg class="search-icon" width="24" height="24" viewBox="0 0 24 24" aria-hidden="true">
    <circle cx="10" cy="10" r="7" fill="none" stroke="#777" stroke-width="2"/>
    <line x1="15" y1="15" x2="21" y2="21" stroke="#777" stroke-width="3" stroke-linecap="round"/>
  </svg>
</div>

<nav class="abs main-nav">
  <a style="left:25px" href="#">Home</a>
  <a style="left:97px" href="#">Laboratory</a>
  <a style="left:205px" href="#">Research</a>
  <a style="left:313px" href="#">Team</a>
  <a style="left:385px" href="#">Press</a>
  <a style="left:457px" href="#">Contact us</a>
</nav>

<div class="abs hero" role="img" aria-label="Laboratory glassware with a pipette releasing a drop">
  <div class="hero-dots"><span></span><span class="is-active"></span><span></span></div>
</div>

<h2 class="abs" style="left:67px;top:479px">Welcome To Our Site</h2>
<div class="abs photo" style="left:77px;top:509px;width:124px;height:95px" role="img" aria-label="Scientist at a microscope"></div>
<p class="abs" style="left:221px;top:513px;width:500px">Lorem Ipsum is simply dummy text of the printing and typesetting industry. Lorem Ipsum has been the industry's standard dummy text ever since the 1500s, when an unknown printer took a galley of type and scrambled it to make a type specimen book. It has survived not only five centuries, but also the leap into electronic typesetting, remaining essentially unchanged.</p>

<h2 class="abs" style="left:67px;top:631px">Lab Describtion</h2>
<p class="abs" style="left:67px;top:660px;width:652px">Lorem Ipsum is simply dummy text of the printing and typesetting industry. Lorem Ipsum has been the industry's standard dummy text ever since the 1500s, when an unknown printer took a galley of type and scrambled it to make a type specimen book. It has survived not only five centuries, but also the leap into electronic typesetting, remaining essentially unchanged. It was popularised in the 1960s with the release of Letraset sheets containing Lorem Ipsum passages, and more recently with desktop publishing software like Aldus PageMaker including versions of Lorem Ipsum.</p>

<div class="abs section-rule"></div>

<h2 class="abs" style="left:67px;top:783px">Our Team Experts</h2>

<div class="abs photo" style="left:73px;top:827px;width:205px;height:116px" role="img" aria-label="Researcher working at a laboratory bench"></div>
<div class="abs member-name" style="left:308px;top:822px">Lorem Ipsum</div>
<p class="abs" style="left:308px;top:856px;width:400px">Lorem Ipsum is simply dummy text of the printing and typesetting industry. Lorem Ipsum has been the industry's standard dummy text ever since the 1500s, when an unknown printer took a galley of type and scrambled it to make a type specimen book.</p>

<div class="abs photo" style="left:73px;top:958px;width:205px;height:116px" role="img" aria-label="Researcher handling lab equipment"></div>
<div class="abs member-name" style="left:308px;top:953px">Lorem Ipsum</div>
<p class="abs" style="left:308px;top:987px;width:400px">Lorem Ipsum is simply dummy text of the printing and typesetting industry. Lorem Ipsum has been the industry's standard dummy text ever since the 1500s, when an unknown printer took a galley of type and scrambled it to make a type specimen book.</p>

<aside class="abs side-box" style="top:460px;height:318px">
  <div class="side-head"><h2>We Find The Right Solutions</h2></div>
  <div class="photo" style="margin:10px 0 0 12px;width:251px;height:118px;background:linear-gradient(135deg,#f4f4f4,#cfcfcf)" role="img" aria-label="Laboratory microscope"></div>
  <p style="margin:20px 12px 0">Lorem Ipsum is simply dummy text of the printing and typesetting industry. Lorem Ipsum has been the industry's standard dummy text ever since the 1500s, when an unknown printer took a galley of type and scrambled it to make a type specimen book.</p>
</aside>

<aside class="abs side-box" style="top:790px;height:218px">
  <div class="side-head"><h2>Research Activity</h2></div>
  <p style="margin:4px 12px 0">Lorem Ipsum is simply dummy text of the printing and typesetting industry. Lorem Ipsum has been the industry's standard dummy text ever since the 1500s, when an unknown printer took a galley of type and scrambled it to make a type specimen book.</p>
</aside>
<a class="abs btn-more" href="#">View More</a>

<footer class="abs site-footer">
  <div class="footer-links"><a href="#">Home</a> |&nbsp; <a href="#">Laboratory</a> &nbsp;|&nbsp; <a href="#">Research</a> &nbsp;|&nbsp; <a href="#">Team</a> &nbsp;|&nbsp; <a href="#">Press</a> &nbsp;|&nbsp; <a href="#">Contact us</a></div>
  <div class="copyright">Copyright@ www.velorastbiologics.com</div>
  <div class="connect">Connect With Us</div>
  <div class="social" aria-label="Social links"><span></span><span></span><span></span><span></span><span></span></div>
</footer>

</body>
</html>
```